Robotic Physical Therapy office needs a Grand Opening Flyer

We need a Grand Opening flyer design for a robotic physical therapy office named Stellar Motion Therapy. We would like it to have a clean, classy, upscale feeling that gives potential clients a V.I.P. feeling. We would like to use the colors black, gray, and yellow (logo will be uploaded).

Event: Thursday, June 1st, 2023 from 12pm-6pm
location: 58274 Harlow Ave, Bloomfield Hills, MI 48319

Industry/Entity Type

Physical therapy

Font styles to use
Script

Colors

Designer to choose colors to be used in the design.

Requirements
Nice to have
• More of a vip feel for the invite

```html
<!DOCTYPE html>
<html lang="en">
<head>
<meta charset="utf-8">
<title>Grand Opening – Stellar Motion Therapy</title>
<link href="https://fonts.googleapis.com/css2?family=Cormorant+Garamond:wght@500&family=Great+Vibes&family=Outfit:wght@700&display=swap" rel="stylesheet">
<style>
  :root {
    --page-bg: #e6e4de;
    --charcoal: #2b2b2d;
    --graphite: #3c3b3d;
    --smoke: #8e8b8b;
    --lemon: #f4e41e;
    --gold-light: #fcecb4;
    --gold-mid: #efc75a;
    --gold-deep: #c38f22;
  }
  * { margin: 0; padding: 0; box-sizing: border-box; }
  html, body { width: 1200px; height: 1200px; overflow: hidden; background: var(--page-bg); }
  .flyer {
    position: absolute; left: 200px; top: 82px; width: 800px; height: 1035px; overflow: hidden;
    background:
      radial-gradient(ellipse 360px 300px at 400px 1060px, rgba(150,152,158,0.75), rgba(150,152,158,0) 100%),
      radial-gradient(ellipse 520px 560px at 400px 380px, var(--smoke) 0%, var(--graphite) 60%, var(--charcoal) 100%);
  }
  .drapes { position: absolute; inset: 0; }
  .flyer > .text, .flyer > .rule, .flyer > .ornament, .flyer > .signoff { position: absolute; }
  .title-grand {
    left: 299px; top: 182px; font-family: "Cormorant Garamond", serif; font-weight: 500;
    font-size: 108px; line-height: 1; color: var(--lemon);
  }
  .title-opening {
    left: 112px; top: 228px; font-family: "Great Vibes", cursive; font-size: 196px;
    line-height: 1; color: var(--lemon); white-space: nowrap;
  }
  .business-tag {
    left: 0; right: 0; top: 466px; display: flex; justify-content: center; align-items: center; gap: 12px;
    font-family: "Outfit", sans-serif; font-weight: 700; font-size: 25px; color: var(--lemon); letter-spacing: 0.2px;
  }
  .business-tag .dash { width: 33px; height: 5px; background: var(--lemon); }
  .ornament {
    background: radial-gradient(ellipse at center, rgba(239,199,90,0.55), rgba(239,199,90,0) 70%);
  }
  .ornament-title { left: 318px; top: 504px; width: 173px; height: 70px; }
  .ornament-location { left: 352px; top: 806px; width: 110px; height: 41px; }
  .event-date, .event-time, .venue-address {
    left: 0; right: 0; text-align: center; font-family: "Outfit", sans-serif; font-weight: 700;
    color: var(--lemon); white-space: nowrap; line-height: 1;
  }
  .event-date { top: 618px; font-size: 42px; padding-left: 14px; }
  .event-date sup { font-size: 20px; vertical-align: 18px; }
  .event-time { top: 676px; font-size: 48px; word-spacing: 4px; }
  .location-label {
    left: 0; right: 0; top: 752px; text-align: center; font-family: "Cormorant Garamond", serif;
    font-weight: 500; font-size: 52px; line-height: 1; color: var(--lemon);
  }
  .venue-address { top: 871px; font-size: 21px; }
  .rule { height: 2px; background: linear-gradient(90deg, rgba(244,228,30,0), var(--lemon) 12%, var(--lemon) 88%, rgba(244,228,30,0)); }
  .rule-date { left: 145px; top: 664px; width: 522px; }
  .rule-address { left: 69px; top: 903px; width: 664px; }
  .signoff {
    left: 280px; top: 920px; width: 244px; height: 91px; border-left: 2px solid var(--lemon); border-right: 2px solid var(--lemon);
    display: flex; align-items: center; justify-content: center; gap: 10px;
  }
  .signoff .dot { width: 30px; height: 30px; border-radius: 50%; background: var(--charcoal); flex: none; }
  .signoff .brand-name {
    font-family: "Outfit", sans-serif; font-weight: 700; font-size: 21px; line-height: 1.05; color: var(--lemon);
  }
</style>
</head>
<body>
  <main class="flyer">
    <svg class="drapes" width="800" height="1035" viewBox="0 0 800 1035" aria-hidden="true">
      <defs>
        <linearGradient id="gold-fold" x1="0" y1="0" x2="0.3" y2="1">
          <stop offset="0" stop-color="var(--gold-light)"/>
          <stop offset="0.55" stop-color="var(--gold-mid)"/>
          <stop offset="1" stop-color="var(--gold-deep)"/>
        </linearGradient>
        <linearGradient id="gold-side" x1="0" y1="0" x2="1" y2="0">
          <stop offset="0" stop-color="var(--gold-deep)"/>
          <stop offset="1" stop-color="var(--gold-light)"/>
        </linearGradient>
      </defs>
      <path d="M0,98 C60,140 180,175 290,166 C430,155 540,80 601,0 H0 Z" fill="url(#gold-fold)"/>
      <path d="M168,0 C200,50 230,80 250,93 C300,75 350,40 384,0 Z" fill="#4a494b"/>
      <path d="M613,0 C640,60 650,160 690,220 C720,270 770,320 800,357 V0 Z" fill="url(#gold-fold)"/>
      <path d="M783,0 C770,80 745,170 742,224 C760,230 785,231 800,231 V0 Z" fill="#333335"/>
      <path d="M0,394 C30,460 30,560 0,640 Z" fill="url(#gold-side)"/>
      <path d="M800,596 C770,660 760,760 800,828 Z" fill="url(#gold-side)"/>
      <path d="M0,1004 C80,1025 180,1030 277,1035 H0 Z" fill="url(#gold-fold)"/>
    </svg>

    <div class="text title-grand">Grand</div>
    <div class="text title-opening">Opening</div>

    <div class="text business-tag"><span class="dash"></span>STELLAR MOTION THERAPY<span class="dash"></span></div>
    <div class="ornament ornament-title" role="img" aria-label="Gold scrollwork flourish"></div>

    <div class="text event-date">THURSDAY, 1<sup>ST</sup> JUNE, 2023</div>
    <div class="rule rule-date"></div>
    <div class="text event-time">• 12PM-6PM •</div>

    <div class="text location-label">Location</div>
    <div class="ornament ornament-location" role="img" aria-label="Small gold scrollwork flourish"></div>

    <div class="text venue-address">58274 HARLOW AVE, BLOOMFIELD HILLS, MI 48319</div>
    <div class="rule rule-address"></div>

    <div class="signoff">
      <span class="dot"></span>
      <span class="brand-name">STELLAR MOTION<br>THERAPY</span>
    </div>
  </main>
</body>
</html>
```